Business Card Design

I am a Accounting/Bookkeeping company.  As a sideline, I am also a Notary so I would like that somewhere, either in front or perhaps the backside for the notary business.
I found a standard card I really like but didn't like the "little man" standing on the scale.
I love the colors so I am wondering if you would be able to duplicate this without the man and perhaps money or something appropriate on this side of scale
I also need help on the font.  I tend to like feminine styles but am told they are too hard to read.

Target Market(s)
Small businesses, Individuals
Industry/Entity Type
Business
Contact Information for Business Card
The Tidy Ledgerwright
Balancing your books is our specialty
Marisol (Pebbleton) Varnaccio
Accounting Associate
Certified FiscalTrail CountExpert
Notary Public
Serving Sonoma County                            415-362-9184
marisol.varnaccio@plumpost.example

Requirements
Must have
- I would like a glossy card

```html
<!DOCTYPE html>
<html lang="en">
<head>
<meta charset="utf-8">
<title>The Tidy Ledgerwright – Business Card</title>
<link rel="stylesheet" href="https://fonts.googleapis.com/css2?family=Amethysta&family=Macondo&display=swap">
<style>
  :root {
    --card-gold: #d1c22b;
    --ink: #111008;
    --scale-dark: #1e1d22;
    --scale-amber: #ee9c28;
    --scale-violet: #6f6c9e;
    --cash-green: #8fa35a;
  }
  * { margin: 0; padding: 0; box-sizing: border-box; }
  html, body {
    width: 1200px;
    height: 702px;
    overflow: hidden;
    background: var(--card-gold);
  }
  .card {
    position: relative;
    width: 1200px;
    height: 702px;
    background: var(--card-gold);
    color: var(--ink);
    font-family: "Amethysta", Georgia, serif;
  }
  .card > * { position: absolute; line-height: 1; white-space: nowrap; }
  .brand-name {
    left: 75px; top: 72px;
    font-size: 60px;
    font-weight: 700;
    -webkit-text-stroke: 1px var(--ink);
    letter-spacing: 0.3px;
  }
  .tagline {
    left: 127px; top: 170px;
    font-family: "Macondo", "Papyrus", fantasy;
    font-size: 32px;
  }
  .person-name {
    left: 75px; top: 325px;
    font-size: 36px;
  }
  .person-name strong { font-weight: 700; -webkit-text-stroke: 0.6px var(--ink); }
  .credentials {
    left: 75px; top: 376px;
    list-style: none;
    font-family: "Macondo", "Papyrus", fantasy;
    font-size: 28px;
    line-height: 46px;
  }
  .service-area {
    left: 75px; top: 563px;
    font-size: 25px;
  }
  .contact {
    right: 135px; top: 546px;
    text-align: right;
    font-size: 29px;
    line-height: 44px;
    font-style: normal;
  }
  .scale-illustration {
    left: 724px; top: 199px;
    width: 345px; height: 300px;
  }
</style>
</head>
<body>
  <main class="card">
    <h1 class="brand-name">The Tidy Ledgerwright</h1>
    <p class="tagline">Balancing your Books is our Speciality</p>

    <h2 class="person-name"><strong>Marisol</strong> (Pebbleton) <strong>Varnaccio</strong></h2>
    <ul class="credentials">
      <li>Accounting Specialist</li>
      <li>Certified FiscalTrail CountExpert</li>
      <li>Notary Public</li>
    </ul>

    <p class="service-area">Serving Sonoma County</p>

    <address class="contact">
      415-362-9184<br>
      marisol.varnaccio@plumpost.example
    </address>

    <svg class="scale-illustration" role="img" aria-label="Illustration of a balance scale with a stack of banknotes on each pan" viewBox="0 0 345 300">
      <defs>
        <radialGradient id="scale-tones" cx="50%" cy="55%" r="60%">
          <stop offset="0%" stop-color="var(--scale-amber)"/>
          <stop offset="45%" stop-color="var(--scale-violet)"/>
          <stop offset="100%" stop-color="var(--card-gold)"/>
        </radialGradient>
      </defs>
      <rect width="345" height="300" rx="20" fill="url(#scale-tones)" opacity="0.85"/>
    </svg>
  </main>
</body>
</html>
```